Redesign website bus travel company Lenz Vals

We require a complete redesign of the website of Reisebüro Lenz Vals, an established bus tour operator based in Graubünden (www.lenzvals-beispiel.ch). For years, the company has specialized in multi-day tours throughout Europe, as well as day trips such as shopping trips to Innsbruck or Como, music tours, and market visits, primarily for seniors, as well as car rentals for clubs and companies.

The new website requires a video header with overlay text, red as the primary corporate color, complemented by black and gray, and a highly simplified navigation with two main sections: "Our Trips" and "Bus Rental." The remaining sections must be accessible via the "Menu" menu item. The design should be user-friendly for all age groups and mobile-responsive.

The goal is a trustworthy, modern website that reflects personal service and many years of experience.
The new logo can be found in the files, as well as a few pictures.

Target Market(s)

Guests of bus tours (day and multi-day trips) and bus rentals (clubs, companies, etc.)

Industry/Entity Type

Busreisen und Busvermietung

Number of Pages Required

1 page

Requirements
Must have
• Red as primary color, video header, simple UX for target group seniors
Nice to have
• Photo galleries of destinations and the vehicle fleet

```html
<!DOCTYPE html>
<html lang="en">
<head>
<meta charset="utf-8">
<title>Lenz Vals – Bus Travel</title>
<link href="https://fonts.googleapis.com/css2?family=Poppins:wght@400;500;600;700&display=swap" rel="stylesheet">
<style>
:root{
  --red:#c8070c;
  --red-dark:#9e0508;
  --black:#0c0c0c;
  --ink:#1d1d1d;
  --gray:#555;
  --light:#fbf1f1;
  --white:#fff;
}
*{box-sizing:border-box;margin:0;padding:0}
html,body{width:1200px;height:3337px;overflow:hidden}
body{font-family:'Poppins',sans-serif;color:var(--ink);background:var(--white);position:relative}
.abs{position:absolute}
.btn{display:inline-flex;align-items:center;justify-content:center;font-family:'Poppins',sans-serif;font-size:12px;font-weight:500;text-decoration:none}
.btn-red{background:var(--red);color:var(--white)}
.btn-outline{border:1px solid var(--red);color:var(--red);background:var(--white)}
.section-title{font-size:40px;font-weight:500;display:flex;align-items:center;gap:8px}
.section-title .rule{display:block;width:92px;height:1px;background:currentColor;opacity:.7}
.rule-red{background:var(--red)!important;opacity:1!important}

/* header */
.site-header{top:0;left:0;width:1200px;height:48px;background:var(--white);display:flex;align-items:center;padding:0 122px;justify-content:space-between}
.brand{font-size:26px;font-weight:700;color:var(--red);letter-spacing:-.5px}
.main-nav{display:flex;align-items:center;gap:30px;font-size:12px}
.main-nav a{color:var(--ink);text-decoration:none}
.main-nav a.active{color:var(--red);border-bottom:1px solid var(--red);padding-bottom:3px}
.main-nav .btn{width:88px;height:26px}

/* hero */
.hero{top:48px;left:0;width:1200px;height:626px;background:linear-gradient(180deg,#203a5c 0%,#5a7fa7 30%,#a6c0d8 45%,#4f7a3a 62%,#c9c230 80%,#6f8f2a 100%);overflow:hidden}
.hero-bus{left:220px;top:270px;width:640px;height:308px;background:linear-gradient(135deg,#1f55b5,#2e7fd8 60%,#b22);border-radius:18px 40px 6px 6px;opacity:.85}
.hero-copy{top:62px;left:0;width:1200px;text-align:center;color:var(--white)}
.hero-copy h1{font-size:48px;font-weight:600;line-height:54px}
.hero-copy h1 em{font-style:normal;color:var(--red)}
.hero-copy p{font-size:12px;margin-top:14px}
.hero-actions{display:flex;justify-content:center;gap:8px;margin-top:24px}
.hero-actions .btn{width:122px;height:26px}
.btn-ghost{border:1px solid rgba(255,255,255,.6);color:var(--white);background:rgba(0,0,0,.2)}
.play{left:566px;top:290px;width:68px;height:68px;border-radius:50%;background:rgba(0,0,0,.55);border:2px solid rgba(255,255,255,.8);display:flex;align-items:center;justify-content:center}

/* about / group */
.split-text h2{font-size:38px;font-weight:500;display:flex;align-items:center;gap:4px}
.split-text h2 .rule{width:92px;height:1px;background:var(--red);display:block;margin-top:10px}
.split-text p{font-size:11.5px;line-height:17.5px;color:#333;margin-top:22px}
.split-text .btn{width:90px;height:26px;margin-top:28px}
.photo-frame{border:1px solid var(--red)}
.photo{display:block}
.watermark{font-size:120px;font-weight:700;color:var(--red);opacity:.05;white-space:nowrap;line-height:1}

/* trips */
.trips{top:1129px;left:0;width:1200px;height:619px;background:linear-gradient(160deg,#3b0b0c 0%,#6b1012 45%,#2a1a1a 100%)}
.trips .section-title{color:var(--white);justify-content:center;position:absolute;top:42px;left:0;width:1200px}
.trip-card{top:135px;width:225px;height:376px;background:var(--white);padding:12px 12px 0}
.trip-card .photo{width:200px;height:168px}
.trip-card h3{font-size:23px;font-weight:600;margin-top:15px}
.trip-date{font-size:11px;font-weight:500;line-height:13px;margin-top:10px;height:26px}
.trip-desc{font-size:9px;color:var(--gray);line-height:14px;margin-top:6px;height:48px}
.trip-foot{display:flex;justify-content:space-between;align-items:center;margin-top:10px}
.trip-foot strong{font-size:13px;font-weight:600}
.trip-foot .btn{width:84px;height:25px}
.trips .view-all{left:549px;top:531px;width:102px;height:25px}

/* rental */
.rental{top:2203px;left:0;width:1200px;height:567px;background:var(--light)}
.rental .section-title{position:absolute;top:42px;left:0;width:1200px;justify-content:center;color:var(--ink)}
.rental-card{top:132px;width:306px;height:315px;background:var(--white)}
.rental-card .photo{width:306px;height:177px}
.rental-body{border-left:3px solid var(--red);padding:18px 16px 0 18px;height:138px;font-size:11.5px;line-height:14px;color:#222}
.rental-body p+p{margin-top:12px}
.rental .view-all{left:549px;top:479px;width:102px;height:25px}

/* cta */
.cta{top:2770px;left:0;width:1200px;height:225px;background:radial-gradient(ellipse at 20% 0%,#d6161b,var(--red) 45%,#a80609 100%);color:var(--white);text-align:center;overflow:hidden}
.cta .section-title{justify-content:center;margin-top:48px;font-size:40px}
.cta p{font-size:12px;margin-top:6px}
.cta-actions{display:flex;justify-content:center;gap:8px;margin-top:18px}
.cta-actions .btn{width:114px;height:26px;background:var(--white);color:var(--ink)}

/* footer */
.site-footer{top:2995px;left:0;width:1200px;height:342px;background:var(--black);color:var(--white)}
.site-footer .brand{position:absolute;left:122px;top:60px;font-size:25px}
.follow{left:122px;top:104px;font-size:12px;font-weight:600}
.socials{left:122px;top:130px;display:flex;gap:10px}
.socials span{width:27px;height:27px;border:1px solid var(--red);border-radius:50%;display:block}
.foot-col{top:62px}
.foot-col h4{font-size:15px;font-weight:600;margin-bottom:18px}
.foot-col li{list-style:none;font-size:11px;margin-bottom:14px}
.foot-col.small li{font-size:10px;margin-bottom:11px}
.contact-col p{font-size:10px;line-height:13px;margin-bottom:12px}
.contact-col .mail{color:var(--red)}
.newsletter p{font-size:11px}
.signup{display:flex;margin-top:30px;width:206px;height:31px}
.signup span{flex:1;border:1px solid var(--red);font-size:11px;padding:8px 14px;background:var(--white);color:#333}
.signup i{width:48px;background:var(--red);display:flex;align-items:center;justify-content:center}
.foot-rule{left:122px;top:268px;width:956px;height:1px;background:#444}
.copyright{left:122px;top:284px;font-size:10px}
.legal{right:122px;top:284px;font-size:10px;display:flex;gap:14px}
</style>
</head>
<body>

<header class="site-header abs">
  <div class="brand">Lenz Vals</div>
  <nav class="main-nav">
    <a class="active">Home</a>
    <a>About Us</a>
    <a>Our Trips <svg width="9" height="6" viewBox="0 0 9 6"><path d="M1 1l3.5 3.5L8 1" fill="none" stroke="#c8070c" stroke-width="1.2"/></svg></a>
    <a>Bus Rental</a>
    <a>Group tours</a>
    <a class="btn btn-red">Contact Us</a>
  </nav>
</header>

<section class="hero abs">
  <div class="hero-bus abs" role="img" aria-label="Touring coach parked in a meadow beside a yellow rapeseed field under blue sky"></div>
  <div class="hero-copy abs">
    <h1><em>Explore</em> Switzerland and Europe<br>with Comfort &amp; Confidence</h1>
    <p>Your trusted bus travel partner for group tours, charters, and custom journeys</p>
    <div class="hero-actions">
      <a class="btn btn-red">Plan Your Trip</a>
      <a class="btn btn-ghost">View Our Fleet</a>
    </div>
  </div>
  <div class="play abs"><svg width="24" height="26" viewBox="0 0 24 26"><path d="M3 1l20 12L3 25z" fill="#fff"/></svg></div>
</section>

<section class="about">
  <div class="watermark abs" style="left:0;top:1020px">Lenz Vals</div>
  <div class="split-text abs" style="left:122px;top:738px;width:430px">
    <h2>About Us <span class="rule"></span></h2>
    <p>The Lenz travel agency has existed for over 60 years and has been run by Marco Tschudi and Peter Caduff, the fourth generation of the family, since August 1, 2013. Our travel industry expertise, friendly and reliable service, and competitive prices set us apart from the competition. Anna Berther, Lea Casutt, and Peter Caduff, our office staff, will be happy to assist you with travel arrangements. Luca Derungs, Jon Arpagaus, and Marco Tschudi, along with other reliable and friendly chauffeurs, will ensure that you reach your destination safely and comfortably.</p>
    <a class="btn btn-red">Learn More</a>
  </div>
  <div class="photo-frame abs" style="left:622px;top:737px;width:456px;height:248px"></div>
  <div class="photo abs" role="img" aria-label="Two company owners smiling beside a coach" style="left:628px;top:744px;width:444px;height:234px;background:linear-gradient(135deg,#4d5a3a,#8c8f86 55%,#2d3540)"></div>
  <div class="photo abs" role="img" aria-label="Couple in traditional dress with alphorn in front of a coach in the mountains" style="left:674px;top:877px;width:352px;height:188px;border:3px solid #fff;background:linear-gradient(180deg,#9fb2c7 0%,#7f8f78 40%,#5f8e35 70%,#4d7a2a 100%)"></div>
</section>

<section class="trips abs">
  <h2 class="section-title"><span class="rule"></span>Our Trips<span class="rule"></span></h2>

  <article class="trip-card abs" style="left:122px">
    <div class="photo" role="img" aria-label="Alphorn player with coach in a mountain meadow" style="background:linear-gradient(180deg,#8ea9c6,#7d8a76 45%,#5c8e3c)"></div>
    <h3>Day trips</h3>
    <p class="trip-date">Wednesday, 10.09.25 - Market in Luino</p>
    <p class="trip-desc">Departure from Vals Dorfplatz (in front of Hotel ABC) at 7:30 a.m. / Return from Tirano at 4:00 p.m.</p>
    <div class="trip-foot"><strong>From &nbsp;€ CHF 52.</strong><a class="btn btn-outline">View Trip</a></div>
  </article>

  <article class="trip-card abs" style="left:365px">
    <div class="photo" role="img" aria-label="Smiling traveller holding a globe" style="background:linear-gradient(135deg,#2c6fb3,#5b97d1 50%,#e7b9a6)"></div>
    <h3>Holiday trips</h3>
    <p class="trip-date">Sunday, 07.09.25 - Market in Cannobio</p>
    <p class="trip-desc">Departure from Vals Dorfplatz (in front of Hotel ABC) at 7:00 a.m. / Return from Cannobio at 3:00 p.m.</p>
    <div class="trip-foot"><strong>From &nbsp;€ CHF 52.</strong><a class="btn btn-outline">View Trip</a></div>
  </article>

  <article class="trip-card abs" style="left:610px">
    <div class="photo" role="img" aria-label="Coach parked under palm trees" style="background:linear-gradient(180deg,#3f7ec9,#8cb4d9 45%,#4d7a35 75%,#7a8a5a)"></div>
    <h3>Club trips</h3>
    <p class="trip-date">Sunday, 08.06.25 - Big Whitsun Market in Tirano</p>
    <p class="trip-desc">Departure from Vals Dorfplatz (in front of Hotel ABC) at 7:30 a.m. / Return from Tirano at 4:00 p.m.</p>
    <div class="trip-foot"><strong>From &nbsp;€ CHF 60.</strong><a class="btn btn-outline">View Trip</a></div>
  </article>

  <article class="trip-card abs" style="left:853px">
    <div class="photo" role="img" aria-label="Tour guide speaking inside a coach aisle" style="background:linear-gradient(180deg,#3a3d44,#6a6e78 50%,#2a2c31)"></div>
    <h3>Wedding trips</h3>
    <p class="trip-date">Friday, 04.07.25 - Summer Breeze on the Island of Mainau</p>
    <p class="trip-desc">Departure from Vals Dorfplatz (in front of Hotel ABC) at 8:00 a.m. / Return from Mainau Island at 4:30 p.m.</p>
    <div class="trip-foot"><strong>From &nbsp;€ CHF 74.</strong><a class="btn btn-outline">View Trip</a></div>
  </article>

  <a class="btn btn-red view-all abs">View all Trips</a>
</section>

<section class="group">
  <div class="photo-frame abs" style="left:122px;top:1810px;width:455px;height:247px"></div>
  <div class="photo abs" role="img" aria-label="Office staff member smiling in front of a coach" style="left:128px;top:1816px;width:443px;height:235px;background:linear-gradient(135deg,#2a5f8a,#8aa0b4 50%,#d9d6d0)"></div>
  <div class="photo abs" role="img" aria-label="Two chauffeurs posing in front of a blue coach" style="left:174px;top:1950px;width:352px;height:188px;border:3px solid #fff;background:linear-gradient(135deg,#2b7fc9,#6fa7d8 45%,#3d3d42)"></div>
  <div class="split-text abs" style="left:648px;top:1815px;width:430px">
    <h2>Group Tours <span class="rule"></span></h2>
    <p style="margin-top:16px">The Lenz travel agency has existed for over 60 years and has been run by Marco Tschudi and Peter Caduff, the fourth generation of the family, since August 1, 2013. Our travel industry expertise, friendly and reliable service, and competitive prices set us apart from the competition. Anna Berther, Lea Casutt, and Peter Caduff, our office staff, will be happy to assist you with travel arrangements. Luca Derungs, Jon Arpagaus, and Marco Tschudi, along with other reliable and friendly chauffeurs, will ensure that you reach your destination safely and comfortably.</p>
    <a class="btn btn-red">Learn More</a>
  </div>
  <div class="watermark abs" style="left:680px;top:2100px">Lenz Vals</div>
</section>

<section class="rental abs">
  <h2 class="section-title"><span class="rule rule-red"></span>Minibus Rental<span class="rule rule-red"></span></h2>

  <article class="rental-card abs" style="left:122px">
    <div class="photo" role="img" aria-label="Silver minibus parked outdoors" style="background:linear-gradient(180deg,#6d7c5a,#b9bcc0 45%,#7b7f84)"></div>
    <div class="rental-body">
      <p>CHF 200.00, basic flat rate per day including 200 km</p>
      <p>Fr. 0.85 per additional kilometer</p>
      <p>(Prices exclude 8.1% VAT, fuel costs and driver)</p>
    </div>
  </article>

  <article class="rental-card abs" style="left:447px">
    <div class="photo" role="img" aria-label="Minibus passenger seats with seat belts" style="background:linear-gradient(180deg,#8a8a88,#5d5d5b 60%,#3d3d3c)"></div>
    <div class="rental-body">
      <p>CHF 200.00, basic flat rate per day including 200 km</p>
      <p>Fr. 0.85 per additional kilometer</p>
      <p>(Prices exclude 8.1% VAT, fuel costs and driver)</p>
    </div>
  </article>

  <article class="rental-card abs" style="left:772px">
    <div class="photo" role="img" aria-label="Silver minibus in front of mountains" style="background:linear-gradient(180deg,#7fa4d0,#c4cdd6 45%,#6f8a4f)"></div>
    <div class="rental-body">
      <p>CHF 200.00, basic flat rate per day including 200 km</p>
      <p>Fr. 0.85 per additional kilometer</p>
      <p>(Prices exclude 8.1% VAT, fuel costs and driver)</p>
    </div>
  </article>

  <a class="btn btn-red view-all abs">View all Rental</a>
</section>

<section class="cta abs">
  <svg class="abs" style="left:0;top:0" width="1200" height="225" viewBox="0 0 1200 225" aria-hidden="true">
    <g fill="none" stroke="#8e0407" stroke-opacity=".35" stroke-width="1">
      <path d="M0 60 C200 20 350 200 600 180 S1000 20 1200 90"/>
      <path d="M0 75 C200 35 350 215 600 195 S1000 35 1200 105"/>
      <path d="M0 90 C200 50 350 230 600 210 S1000 50 1200 120"/>
      <path d="M0 105 C200 65 350 245 600 225 S1000 65 1200 135"/>
    </g>
  </svg>
  <h2 class="section-title" style="position:relative"><span class="rule"></span>Ready to Travel?<span class="rule"></span></h2>
  <p style="position:relative">Get a personalized quote or speak to our travel advisors today.</p>
  <div class="cta-actions" style="position:relative">
    <a class="btn">Request a Quote</a>
    <a class="btn">Contact Us</a>
  </div>
</section>

<footer class="site-footer abs">
  <div class="brand">Lenz Vals</div>
  <p class="follow abs">Follow Us</p>
  <div class="socials abs"><span></span><span></span><span></span></div>

  <div class="foot-col abs" style="left:369px">
    <h4>Useful Links</h4>
    <ul><li>Home</li><li>About Us</li><li>Our Trips</li><li>Bus Rental</li><li>Group tours</li></ul>
  </div>
  <div class="foot-col small abs" style="left:511px">
    <h4>Our Trips</h4>
    <ul><li>Day trips</li><li>Holiday trips</li><li>Club trips</li><li>Wedding trips</li></ul>
  </div>
  <div class="foot-col contact-col abs" style="left:661px;width:170px">
    <h4>Contact us</h4>
    <p>Monday - Friday<br>8:00 a.m. - 12:00 p.m. &amp; 1:30 p.m. - 5:00 p.m.</p>
    <p>Phone: 081 000 12 34</p>
    <p class="mail">info@lenzvals-beispiel.ch</p>
  </div>
  <div class="foot-col newsletter abs" style="left:872px">
    <h4>Newsletter</h4>
    <p>Subscribe to our newsletter</p>
    <div class="signup"><span>Email</span><i><svg width="20" height="18" viewBox="0 0 20 18"><path d="M1 8l18-7-4 16-6-5-3 4v-5l9-8-11 7z" fill="none" stroke="#fff" stroke-width="1.2" stroke-linejoin="round"/></svg></i></div>
  </div>

  <div class="foot-rule abs"></div>
  <p class="copyright abs">Copyright © 2025 Nordweb. All rights reserved.</p>
  <div class="legal abs"><span>Company</span><span>Privacy Policy</span><span>Terms and Conditions</span></div>
</footer>

</body>
</html>
```